Simple but strong message business card.

I will be using this to communicate a message about how we are different from our main competitor. I will be giving these out at a trade show. It needs to have our logo and then communicate that we do not charge PCI Fees. Our competitor charges junk fees at an exorbitant amount and our target audience is aware of it and tired of the BS.

Target Market(s)

Attendees of a trade show. General managers of the ridgeline growers union. www.fieldhallmark.net

Contact Information for Business Card

Font styles to use
Sans Serif

Colors

Designer to choose colors to be used in the design.

Requirements
Must have
• Our logo. and the message of No PCI Fees
• contact email - tbrolin@quillmerchant.net
• contact name - Dane Brolin
• contact phone - 303-555-0142

```html
<!DOCTYPE html>
<html lang="en">
<head>
<meta charset="utf-8">
<title>Quill Merchant – Business Card</title>
<link rel="stylesheet" href="https://fonts.googleapis.com/css2?family=Lato:wght@400;700;900&display=swap">
<style>
  :root {
    --bg: #1b1b1b;
    --card: #141414;
    --card-edge: #222222;
    --green: #7dc242;
    --text-light: #e6e6e6;
    --text-grey: #9a9a9a;
    --rule: #4a4a4a;
  }
  * { box-sizing: border-box; margin: 0; padding: 0; }
  html, body {
    width: 1200px; height: 900px; overflow: hidden;
    background: var(--bg);
    font-family: "Lato", sans-serif;
  }
  .sheet {
    width: 1200px; height: 900px;
    display: flex; flex-direction: column;
    align-items: center; justify-content: center; gap: 50px;
  }
  .card {
    position: relative;
    width: 630px; height: 360px;
    background: var(--card);
    border: 1px solid var(--card-edge);
    border-radius: 22px;
    box-shadow: 0 18px 40px rgba(0,0,0,0.55);
    overflow: hidden;
  }

  /* Back side */
  .card-back .brand {
    position: absolute; top: 120px; left: 0; right: 0;
    text-align: center;
    font-weight: 700; font-size: 40px; letter-spacing: 2px;
    text-transform: uppercase; color: var(--text-light);
  }
  .card-back .message {
    position: absolute; top: 215px; left: 90px; right: 90px;
    display: flex; align-items: center; gap: 18px;
    color: var(--text-light); font-weight: 700; font-size: 20px; letter-spacing: 0.5px;
  }
  .card-back .message::before,
  .card-back .message::after {
    content: ""; flex: 1; height: 1px; background: var(--rule);
  }

  /* Front side */
  .card-front .brand {
    position: absolute; top: 48px; right: 50px;
    font-weight: 700; font-size: 30px; letter-spacing: 1.5px;
    text-transform: uppercase; color: var(--green);
  }
  .card-front .divider {
    position: absolute; top: 112px; left: 50px; right: 50px;
    height: 1px; background: var(--rule);
  }
  .card-front .message {
    position: absolute; top: 140px; right: 50px;
    color: var(--green); font-weight: 700; font-size: 22px; letter-spacing: 0.5px;
  }
  .card-front .person {
    position: absolute; left: 50px; bottom: 44px;
  }
  .person .name {
    color: var(--green); font-weight: 900; font-size: 28px;
    text-transform: uppercase; letter-spacing: 0.5px; margin-bottom: 18px;
  }
  .contact-line {
    display: flex; align-items: center; gap: 10px;
    color: var(--text-light); font-size: 18px; line-height: 1.6;
  }
  .contact-line svg { width: 18px; height: 18px; fill: var(--green); }
</style>
</head>
<body>
  <main class="sheet">
    <section class="card card-back">
      <div class="brand">Quill Merchant</div>
      <div class="message">NO PCI FEES</div>
    </section>

    <section class="card card-front">
      <div class="brand">Quill Merchant</div>
      <div class="divider"></div>
      <div class="message">NO PCI FEES</div>
      <div class="person">
        <div class="name">Dane Brolin</div>
        <div class="contact-line">
          <svg viewBox="0 0 24 24" aria-hidden="true"><path d="M6.6 10.8a15.1 15.1 0 0 0 6.6 6.6l2.2-2.2a1 1 0 0 1 1-.25 11.4 11.4 0 0 0 3.6.57 1 1 0 0 1 1 1V20a1 1 0 0 1-1 1A17 17 0 0 1 3 4a1 1 0 0 1 1-1h3.5a1 1 0 0 1 1 1c0 1.25.2 2.45.57 3.57a1 1 0 0 1-.25 1z"/></svg>
          <span>303-555-0142</span>
        </div>
        <div class="contact-line">
          <svg viewBox="0 0 24 24" aria-hidden="true"><path d="M3 5h18a1 1 0 0 1 1 1v12a1 1 0 0 1-1 1H3a1 1 0 0 1-1-1V6a1 1 0 0 1 1-1zm1 2.3V17h16V7.3l-8 5.2z M4.6 7h14.8L12 11.8z"/></svg>
          <span>tbrolin@quillmerchant.net</span>
        </div>
      </div>
    </section>
  </main>
</body>
</html>
```